Presentation pour application de menu digitale

Je souhaite créer un flyer de présentation pour une application de menu digitale afin de la présenter à mes futurs clients. Cette application aura aussi vocation de premier réseau social culinaire pour les utilisateurs finaux.
Merci de récupérer le texte du site platboreal.tech
Le flyer sera imprimé au format A3 pliable pour en faire un format A4.
Le logo et les images que vous récupérerez seront en vernis sélectif.

Target Market(s)

restaurateur

Industry/Entity Type

Restaurateur

Font styles to use
Sans Serif

Colors
59FF00
82FF00
B8FF75
E3FFCB
F4FFEA
6B429C
8869AF
B7A5CE
E3DAEB
F3F0F8

```html
<!DOCTYPE html>
<html lang="fr">
<head>
<meta charset="utf-8">
<title>PlatBoréal – Dépliant de présentation</title>
<link href="https://fonts.googleapis.com/css2?family=Fira+Sans:wght@300;400;500;600;700;800&display=swap" rel="stylesheet">
<style>
  :root{
    --purple:#774e9f;
    --mint:#76c4a4;
    --ink:#0b0b0b;
    --paper:#ffffff;
    --backdrop:#ececec;
    --dark-photo:#1d2430;
  }
  *{box-sizing:border-box;margin:0;padding:0}
  html,body{width:1200px;height:904px;overflow:hidden;background:var(--backdrop)}
  body{font-family:"Fira Sans",Arial,sans-serif;color:var(--ink)}
  .spread{position:absolute;left:0;top:28px;width:1200px;height:848px;background:var(--paper);overflow:hidden}
  .spread-shapes{position:absolute;inset:0}
  .intro{position:absolute;left:56px;top:50px;width:490px;color:#fff;font-weight:300;font-size:13px;line-height:17px}
  .intro p+p{margin-top:17px}
  .intro strong{font-weight:600}
  .contact{position:absolute;left:56px;top:500px;width:240px;font-size:14.5px;line-height:18.2px;font-weight:500}
  .phone{position:absolute;border-radius:13px;border:3px solid #c9c2b2;box-shadow:0 10px 14px rgba(0,0,0,.18)}
  .phone--menu{background:linear-gradient(180deg,#6d6a62 0%,#6d6a62 24%,#c9a88a 25%,#9c8b6f 55%,#d98c7c 80%,#e7c37c 100%)}
  .phone--splash{background:linear-gradient(160deg,#ffffff 0%,#f6f6f4 60%,#eef1ea 100%)}
  .brand-name{position:absolute;font-weight:700;color:var(--ink);letter-spacing:-.5px;display:flex;align-items:center;white-space:nowrap}
  .brand-name .dot{display:inline-block;border-radius:50%;background:var(--mint);margin-right:10px}
  .brand-name--back{left:46px;top:738px;font-size:40px}
  .brand-name--back .dot{width:30px;height:30px}
  .brand-name--cover{left:640px;top:528px;font-size:54px}
  .brand-name--cover .dot{width:40px;height:40px}
  .band{position:absolute;top:789px;height:35px;background:var(--mint)}
  .band--left{left:0;width:37px}
  .band--mid{left:275px;width:720px}
  .band--right{left:1163px;width:37px}
  .url{position:absolute;top:789px;height:35px;line-height:35px;font-size:15.5px;font-weight:500}
  .url--back{left:275px;width:432px;text-align:center;color:#fff}
  .url--cover{left:995px;width:168px;text-align:center;color:var(--ink)}
  .cover-title{position:absolute;left:636px;top:682px;font-size:38px;font-weight:700;color:var(--purple);letter-spacing:-.3px}
  .cover-sub{position:absolute;left:637px;top:728px;font-size:26px;font-weight:600;color:var(--ink)}
</style>
</head>
<body>
<main class="spread">
  <svg class="spread-shapes" width="1200" height="848" viewBox="0 0 1200 848">
    <defs>
      <linearGradient id="bowlsTone" x1="0" y1="0" x2="1" y2="1">
        <stop offset="0" stop-color="#27303d"/>
        <stop offset=".45" stop-color="#3b4a3a"/>
        <stop offset=".7" stop-color="#5b3c3c"/>
        <stop offset="1" stop-color="#1b2029"/>
      </linearGradient>
    </defs>
    <rect class="purple-field" width="1200" height="848" fill="var(--purple)"/>
    <path class="white-field" fill="#fff" d="M0,246 C170,350 400,480 600,470 C660,466 700,445 722,414 L1200,132 L1200,848 L0,848 Z"/>
    <path class="black-sweep black-sweep--back" fill="var(--ink)" d="M0,258 C110,322 215,392 300,429 C280,440 245,437 222,428 C140,398 60,352 0,318 Z"/>
    <path class="black-sweep black-sweep--cover" fill="var(--ink)" d="M728,418 L1200,143 L1200,395 C1100,448 1020,490 963,517 C880,488 790,452 728,418 Z"/>
    <polygon class="hero-photo" role="img" aria-label="Photo vue de dessus de bols d'ingrédients frais : concombre, edamame, saumon, radis, riz" points="895,40 1107,160 1107,370 895,490 683,370 683,160" fill="url(#bowlsTone)" stroke="#fff" stroke-width="11" stroke-linejoin="round"/>
  </svg>

  <section class="intro">
    <p>Plongez au cœur d’une révolution culinaire avec notre application de menu digital, conçue pour enrichir votre expérience au restaurant. PlatBoréal va au-delà d’un simple menu : c’est une plateforme où vous pouvez préparer vos commandes, sauvegarder vos plats favoris, et partager vos expériences avec vos amis. En d’autre termes, <strong>le premier réseau social pour restaurants.</strong></p>
    <p>Plongez au cœur d’une révolution culinaire avec notre application de menu digital, conçue pour enrichir votre expérience au restaurant. PlatBoréal va au-delà d’un simple menu : <strong>c’est une plateforme où vous pouvez préparer vos commandes, sauvegarder vos plats favoris, et partager vos expériences avec vos amis. En d’autre termes, le premier réseau social pour restaurants</strong></p>
  </section>

  <div class="phone phone--menu" role="img" aria-label="Smartphone affichant le menu de l'application par catégories" style="left:319px;top:353px;width:107px;height:263px"></div>
  <div class="phone phone--splash" role="img" aria-label="Smartphone affichant l'écran d'accueil de l'application" style="left:451px;top:352px;width:118px;height:262px;transform:rotate(3deg)"></div>

  <p class="contact">Pour intégrer PlatBoréal dans votre restaurant ou pour toute demande d’information, souscrivez a l’un des abonnements ci-dessus ou contactez nous à [email/contact] ou appelez nous au: [numéro de téléphone].</p>

  <div class="brand-name brand-name--back"><span class="dot"></span>PlatBoréal</div>

  <div class="phone phone--menu" role="img" aria-label="Smartphone affichant le menu de l'application par catégories" style="left:910px;top:393px;width:108px;height:270px"></div>
  <div class="phone phone--splash" role="img" aria-label="Smartphone affichant l'écran d'accueil de l'application" style="left:1045px;top:393px;width:118px;height:270px;transform:rotate(3deg)"></div>

  <div class="brand-name brand-name--cover"><span class="dot"></span>PlatBoréal</div>

  <h1 class="cover-title">Bienvenue sur PlatBoréal</h1>
  <p class="cover-sub">Le 1er réseau social culinaire</p>

  <div class="band band--left"></div>
  <div class="band band--mid"></div>
  <div class="band band--right"></div>
  <span class="url url--back">www.platboreal.tech</span>
  <span class="url url--cover">www.platboreal.tech</span>
</main>
</body>
</html>
```